Business Card Design

We would like a business card that utilizes our current logo and keeps with the same feel - elegant and organic. Our farm isn't about mass production, it's about excellence, education, beautiful events and flowers - people, culture, and community.

Target Market(s)

Patrons to our farm who are interested in weddings, events, or our flowers and vegetables.

Contact Information for Business Card

Name, address, cell email (Danielle Hoskins, 2716 Wrenfield Rd, Harlow Springs, CO 80417, cell 30.412.6638, email danielle@wrenfieldacres.com)

```html
<!DOCTYPE html>
<html lang="en">
<head>
<meta charset="utf-8">
<title>Wrenfield Acres — Business Card</title>
<link href="https://fonts.googleapis.com/css2?family=Marcellus&family=Montserrat:wght@300;400;600&display=swap" rel="stylesheet">
<style>
  :root {
    --backdrop: #d3cdd0;
    --forest: #394f3d;
    --sage: #a4bda7;
    --sage-deep: #6f8f74;
    --wheat: #b78a4c;
    --cream: #ece7db;
    --ink: #3b3f3a;
  }
  * { margin: 0; padding: 0; box-sizing: border-box; }
  html, body { width: 1200px; height: 1200px; overflow: hidden; }
  body {
    background: var(--backdrop);
    font-family: "Montserrat", sans-serif;
    position: relative;
  }
  .card {
    position: absolute;
    left: 180px;
    width: 840px;
    height: 480px;
    border-radius: 4px;
    box-shadow: 0 10px 30px rgba(40, 40, 40, 0.18);
    overflow: hidden;
  }
  .card--front { top: 90px; background: var(--forest); }
  .card--back { top: 630px; background: var(--cream); }

  .wordmark {
    font-family: "Montserrat", sans-serif;
    font-weight: 300;
    letter-spacing: 0.18em;
    text-transform: uppercase;
    display: flex;
    align-items: center;
    gap: 18px;
    white-space: nowrap;
  }
  .wordmark__dot {
    width: 14px; height: 14px; border-radius: 50%;
    background: currentColor;
  }
  .card--front .wordmark {
    position: absolute;
    top: 180px; left: 0; right: 0;
    justify-content: center;
    color: var(--sage);
    font-size: 46px;
  }
  .front__url {
    position: absolute;
    bottom: 62px; left: 0; right: 0;
    text-align: center;
    color: #dfe6dc;
    font-size: 17px;
    font-weight: 300;
    letter-spacing: 0.32em;
  }

  .back__decor {
    position: absolute;
    right: -60px; bottom: -80px;
    width: 420px; height: 320px;
    border-radius: 50%;
    background: radial-gradient(ellipse at center, rgba(164,189,167,0.18), rgba(164,189,167,0) 70%);
  }
  .card--back .wordmark {
    position: absolute;
    left: 60px; top: 210px;
    color: var(--sage-deep);
    font-size: 26px;
    gap: 12px;
  }
  .card--back .wordmark__dot { width: 9px; height: 9px; }

  .contact {
    position: absolute;
    left: 470px; top: 110px;
    width: 330px;
    color: var(--ink);
  }
  .contact__name {
    font-family: "Marcellus", serif;
    font-weight: 400;
    font-size: 36px;
    color: var(--sage-deep);
    line-height: 1.1;
    padding-bottom: 8px;
    border-bottom: 2px solid var(--sage-deep);
  }
  .contact__title {
    margin-top: 8px;
    font-weight: 600;
    font-size: 15px;
    color: var(--wheat);
    letter-spacing: 0.04em;
  }
  .contact__list { list-style: none; margin-top: 24px; }
  .contact__item {
    display: flex;
    align-items: flex-start;
    gap: 14px;
    font-size: 14px;
    line-height: 1.35;
    margin-bottom: 12px;
  }
  .contact__icon { width: 16px; height: 16px; flex: none; margin-top: 1px; fill: var(--forest); }
</style>
</head>
<body>

  <section class="card card--front" aria-label="Card front">
    <div class="wordmark"><span class="wordmark__dot"></span>Wrenfield Acres</div>
    <p class="front__url">www.wrenfieldacres.com</p>
  </section>

  <section class="card card--back" aria-label="Card back">
    <div class="back__decor" role="img" aria-label="Faint leaf pattern decoration"></div>
    <div class="wordmark"><span class="wordmark__dot"></span>Wrenfield Acres</div>

    <div class="contact">
      <h1 class="contact__name">Danielle Hoskins</h1>
      <p class="contact__title">CEO &amp; FOUNDER</p>
      <ul class="contact__list">
        <li class="contact__item">
          <svg class="contact__icon" viewBox="0 0 24 24" aria-hidden="true"><path d="M6.6 10.8a15 15 0 0 0 6.6 6.6l2.2-2.2a1 1 0 0 1 1-.25 11.4 11.4 0 0 0 3.6.57 1 1 0 0 1 1 1V20a1 1 0 0 1-1 1A17 17 0 0 1 3 4a1 1 0 0 1 1-1h3.5a1 1 0 0 1 1 1c0 1.25.2 2.45.57 3.57a1 1 0 0 1-.25 1z"/></svg>
          <span>30.412.6638</span>
        </li>
        <li class="contact__item">
          <svg class="contact__icon" viewBox="0 0 24 24" aria-hidden="true"><path d="M2 5h20v14H2z"/><path d="M3 6.5l9 7 9-7V6H3z" fill="var(--cream)"/></svg>
          <span>danielle@wrenfieldacres.com</span>
        </li>
        <li class="contact__item">
          <svg class="contact__icon" viewBox="0 0 24 24" aria-hidden="true"><path d="M12 2a7 7 0 0 0-7 7c0 5.2 7 13 7 13s7-7.8 7-13a7 7 0 0 0-7-7zm0 9.5A2.5 2.5 0 1 1 12 6.5a2.5 2.5 0 0 1 0 5z"/></svg>
          <span>2716 Wrenfield Rd,<br>Harlow Springs, CO 80417</span>
        </li>
      </ul>
    </div>
  </section>

</body>
</html>
```